Brightpath EAP 2 x Flyer with Poster

Brightpath is an award-winning organisation providing dynamic and creative ways for children, young people, adults and families to make positive change and achieve fulfilling lives.
We are launching into a new area of business and starting to offer organisations Employee Assistance Program (EAP). To launch this service we need 2 flyers and a poster:
- 1 x flyer for employers
- 1 x flyer for employees
- 1 x poster (A3) for employees to be displayed around the office.
For the flyers we are after an a4 colour double sided flyer in either a A4 tri-fold to DL format or A4 bi-fold to A5 format. We are looking for a design that is simple and dynamic whilst keeping in line with our branding.
The winning designs will need to be hi-res and ready for print and also a lower res version suitable to email.
I have attached a number of files to provide further background, including:
• I have attached 3 x word doc of copy for each (2 x flyer / 1 x poster)
• Brand Guidelines
• Logo
• Our clinic flyer recently produced by a ArtHive designer for our clinic area of the business. These flyers do not have to be exactly the same as this one but should appear to be from the same organisation although a different service.
Generally we like our designs to be clear and simple.
Please don't hesitate to reach out with any Q's.

```html
<!DOCTYPE html>
<html lang="en">
<head>
<meta charset="utf-8">
<title>Brightpath EAP Poster</title>
<link href="https://fonts.googleapis.com/css2?family=Poppins:wght@400;500;600;700;800&display=swap" rel="stylesheet">
<style>
:root{
  --green:#5a7560;
  --teal:#7c9fa4;
  --pink:#d5a897;
  --pink-light:#f7e3da;
  --grey-bg:#9a9a9a;
  --chevron:#e4e4e4;
  --ink:#2b2b2b;
  --white:#ffffff;
}
*{margin:0;padding:0;box-sizing:border-box}
html,body{width:707px;height:1200px;overflow:hidden;background:var(--grey-bg);font-family:'Poppins',sans-serif}
.poster{position:absolute;left:0;top:100px;width:707px;height:1000px;background:var(--white);overflow:hidden;color:var(--ink)}
.abs{position:absolute}
.header-art{position:absolute;left:0;top:0;width:707px;height:360px}
.brand{left:44px;top:44px;display:flex;align-items:center;gap:10px}
.brand-dot{width:40px;height:40px;border-radius:50%;background:var(--green)}
.brand-name{font-size:36px;font-weight:600;color:#3a3a3a;line-height:1}
.title{left:34px;top:125px;font-size:45px;font-weight:800;line-height:43px;color:var(--white);letter-spacing:.3px}
.subtitle{left:34px;top:273px;font-size:18.5px;font-weight:700;line-height:21px;color:var(--pink-light)}
.col{top:357px;border-left:2px solid var(--teal);padding-left:8px}
.col h2{font-size:17.5px;font-weight:700;line-height:17px;color:var(--teal);margin-bottom:4px}
.col p{font-size:9.2px;line-height:11.2px}
.col-about{left:34px;width:300px}
.col-eap{left:368px;width:300px}
.services{left:34px;top:477px;width:639px;height:197px;background:var(--green);border-radius:8px;color:var(--white)}
.services-art{position:absolute;left:262px;top:68px;width:130px;height:129px;background:linear-gradient(180deg,#6c8571 0%,#5f5a4e 55%,#6b6a5e 100%)}
.services-tab{left:194px;top:-5px;width:252px;height:38px}
.services-tab span{position:absolute;inset:0;display:flex;align-items:center;justify-content:center;font-size:16.5px;font-weight:700;color:var(--white)}
.services-intro{left:30px;top:45px;font-size:10.3px;font-weight:600}
.services ul{position:absolute;list-style:none;font-size:10.3px;font-weight:500;line-height:16px}
.services li{position:relative;padding-left:12px}
.services li::before{content:"";position:absolute;left:0;top:6px;width:5px;height:5px;border-radius:50%;background:var(--pink)}
.services li.plain::before{display:none}
.list-left{left:34px;top:62px}
.list-right{left:434px;top:62px}
.card{top:714px;width:208px;height:192px;border-radius:8px;color:var(--white);text-align:center}
.card-pay{left:34px;background:var(--teal)}
.card-conf{left:250px;background:var(--pink)}
.card-book{left:465px;background:var(--teal)}
.card-head{position:absolute;left:0;top:36px;width:100%;height:29px;background:var(--green);display:flex;align-items:center;justify-content:center;font-size:11px;font-weight:600;line-height:11px;padding:0 20px}
.card-body{position:absolute;left:12px;right:12px;top:71px;font-size:9px;line-height:10.8px}
.card-icon{position:absolute;left:50%;top:-26px;margin-left:-24px;width:48px;height:48px;border-radius:50%;background:var(--green);border:3px solid var(--white);display:flex;align-items:center;justify-content:center}
.card-contact{font-size:11.5px;font-weight:500;margin-top:3px}
.footer-art{position:absolute;left:0;top:918px;width:707px;height:82px}
.footer-name{left:36px;top:941px;font-size:24px;font-weight:600;color:var(--white)}
.footer-phone{left:208px;top:946px;font-size:15.5px;font-weight:600;color:var(--white);display:flex;align-items:center;gap:4px}
.footer-web{left:372px;top:943px;font-size:8.8px;font-weight:500;line-height:14px;color:var(--white)}
.footer-addr{left:496px;top:943px;font-size:8.8px;font-weight:500;line-height:12px;color:var(--white);display:flex;gap:4px;align-items:flex-start}
.footer-addr svg{margin-top:1px;flex:none}
</style>
</head>
<body>
<div class="poster">

  <svg class="header-art" viewBox="0 0 707 360" aria-hidden="true">
    <polygon points="580,0 630,0 668,35 630,75 580,75 618,35" fill="var(--chevron)"/>
    <polygon points="650,0 707,0 707,75 650,75 688,35" fill="var(--chevron)"/>
    <path d="M0,112 H352 Q362,112 366,120 L424,225 L366,330 Q362,339 352,339 H0 Z" fill="var(--green)"/>
    <polygon points="0,270 399,270 372,320 0,320" fill="var(--pink)"/>
  </svg>
  <svg class="abs" style="left:364px;top:106px" width="343" height="240" viewBox="0 0 343 240" role="img" aria-label="Black and white photo of several hands forming a star shape on grass">
    <defs><radialGradient id="photoTone" cx="50%" cy="50%" r="70%"><stop offset="0" stop-color="#5a5a5a"/><stop offset="1" stop-color="#2a2a2a"/></radialGradient></defs>
    <polygon points="8,0 343,0 343,240 0,240 70,120" fill="url(#photoTone)"/>
  </svg>

  <div class="abs brand"><span class="brand-dot"></span><span class="brand-name">Brightpath</span></div>

  <h1 class="abs title">EMPLOYEE<br>ASSISTANCE<br>PROGRAM (EAP)</h1>
  <div class="abs subtitle">COUNSELLING FOR WORK RELATED<br>OR PERSONAL ISSUES</div>

  <section class="abs col col-about">
    <h2>ABOUT BRIGHTPATH</h2>
    <p>Brightpath provides a confidential and effective counselling process that is solution-focused and practical. The service is aimed at enhancing wellbeing and mental health, and can be accessed via face-to-face consultations, and by Telehealth or phone. Accessing assistance is an act of independence and strength which can empower you to make positive changes in your life.</p>
  </section>
  <section class="abs col col-eap">
    <h2>EMPLOYEE<br>ASSISTANCE PROGRAM</h2>
    <p>Employee Assistance Program (EAP) is a confidential employer-funded support service available to employees and immediate family members experiencing personal or work-related concerns. Immediate family include your spouse, partner, children or others living in your household.</p>
  </section>

  <section class="abs services">
    <div class="services-art" role="img" aria-label="Photo of a parent and child sitting side by side, seen from behind"></div>
    <svg class="abs services-tab" viewBox="0 0 252 38" aria-hidden="true"><polygon points="0,0 252,0 240,38 12,38" fill="var(--teal)"/></svg>
    <div class="abs services-tab"><span>COUNSELLING SERVICES</span></div>
    <div class="abs services-intro">EAP IS PROVIDED FOR A VARIETY OF PERSONAL, EMOTIONAL AND WORK-RELATED MATTERS INCLUDING:</div>
    <ul class="list-left">
      <li>Anxiety</li>
      <li>Depression and emotional wellbeing</li>
      <li>Workplace conflict or disharmony</li>
      <li>Coping with organisational change</li>
      <li>Stress and burnout</li>
      <li>Bullying</li>
      <li>Sexual harassment</li>
      <li>Self-esteem</li>
    </ul>
    <ul class="list-right" style="line-height:12.5px">
      <li>Reactions to traumatic or<br>distressing events</li>
      <li style="margin-top:3.5px">Critical incidents</li>
      <li style="margin-top:3.5px">Grief and bereavement</li>
      <li style="margin-top:3.5px">Substance misuse</li>
      <li style="margin-top:3.5px">Domestic violence</li>
      <li style="margin-top:3.5px">Interpersonal relationships</li>
      <li class="plain" style="margin-top:3.5px">Schooling and study difficulties</li>
    </ul>
  </section>

  <article class="abs card card-pay">
    <div class="card-icon"><svg width="24" height="24" viewBox="0 0 24 24" fill="none" stroke="#fff" stroke-width="1.6"><circle cx="14" cy="7" r="5"/><path d="M2 16h5l4 2h6l4-3M2 21h6l3 1h5" stroke-linecap="round"/></svg></div>
    <div class="card-head">WHO PAYS FOR THE SERVICE?</div>
    <div class="card-body">Your employer will pay for an agreed number of sessions. You are not required to pay for using the Brightpath EAP service. The number of available sessions depends on the agreement we have with your employer.</div>
  </article>
  <article class="abs card card-conf">
    <div class="card-icon"><svg width="24" height="24" viewBox="0 0 24 24" fill="none" stroke="#fff" stroke-width="1.8"><rect x="5" y="11" width="14" height="11" rx="2"/><path d="M8 11V7a4 4 0 0 1 8 0v4"/></svg></div>
    <div class="card-head">IS IT CONFIDENTIAL?</div>
    <div class="card-body">All employee personal information collated by Brightpath during the provision of counselling services will remain confidential and secure except when subpoenaed by a court or failure to disclose the information would place the employee and/or another person at risk. Confidentiality and limitations of confidentiality are explained to employees at the beginning of the counselling process.</div>
  </article>
  <article class="abs card card-book">
    <div class="card-icon"><svg width="24" height="24" viewBox="0 0 24 24" fill="none" stroke="#fff" stroke-width="1.6"><rect x="3" y="5" width="18" height="16" rx="2"/><path d="M3 10h18M8 3v4M16 3v4M9 15l2 2 4-4"/></svg></div>
    <div class="card-head">HOW DO I MAKE AN EAP APPOINTMENT?</div>
    <div class="card-body">You can make a confidential appointment directly with Brightpath through our direct line on
      <div class="card-contact">03 5550 1234</div>
      <div>or via</div>
      <div class="card-contact">clinic@brightpath.au</div>
    </div>
  </article>

  <svg class="footer-art" viewBox="0 0 707 82" aria-hidden="true">
    <polygon points="0,0 204,0 184,41 204,82 0,82" fill="var(--green)"/>
    <polygon points="224,9 707,9 707,73 224,73 204,41" fill="var(--teal)"/>
  </svg>
  <div class="abs footer-name">Brightpath</div>
  <div class="abs footer-phone"><svg width="14" height="14" viewBox="0 0 24 24" fill="none" stroke="var(--pink-light)" stroke-width="2"><path d="M5 3h4l2 5-3 2a12 12 0 0 0 6 6l2-3 5 2v4a2 2 0 0 1-2 2A17 17 0 0 1 3 5a2 2 0 0 1 2-2z"/></svg>(03) 5550 1234</div>
  <div class="abs footer-web">✉ clinic@brightpath.au<br>◍ www.brightpath.au</div>
  <div class="abs footer-addr"><svg width="9" height="11" viewBox="0 0 24 28" fill="var(--pink)"><path d="M12 0a10 10 0 0 0-10 10c0 8 10 18 10 18s10-10 10-18A10 10 0 0 0 12 0zm0 14a4 4 0 1 1 0-8 4 4 0 0 1 0 8z"/></svg><span>Harbourview Building<br>42 Wattle St, Northcote VIC 3070</span></div>

</div>
</body>
</html>
```